Business Card & Letterhead Design

We a financial advice company based in Australia. We provide advice to wealthy farmers.

We are changing our business name FROM Brightmere Financial TO Calderstone Wealth and we need a new letterhead and double sided business card design

Attached is designs from our previous branding (Brightmere Financial) as it includes all the details we require on the new Calderstone Wealth business cards and letterhead.

```html
<!DOCTYPE html>
<html lang="en">
<head>
<meta charset="utf-8">
<title>Calderstone Wealth Letterhead</title>
<link href="https://fonts.googleapis.com/css2?family=Lato:wght@400;700&display=swap" rel="stylesheet">
<style>
  :root {
    --slate: #5d6a72;
    --charcoal: #4a4a4a;
    --ink: #333333;
    --paper: #ffffff;
    --page-bg: #ffffff;
  }
  * { margin: 0; padding: 0; box-sizing: border-box; }
  html, body { width: 1200px; height: 1000px; overflow: hidden; background: var(--page-bg); }
  body { font-family: 'Lato', Arial, sans-serif; position: relative; }
  .letterhead { position: absolute; inset: 0; }
  .shapes { position: absolute; left: 0; top: 0; width: 1200px; height: 1000px; }
  .brand { position: absolute; left: 680px; top: 0; width: 250px; height: 150px; text-align: center; color: var(--paper); }
  .brand-name { position: absolute; left: 0; right: 0; top: 106px; font-size: 17px; font-weight: 400; letter-spacing: 1px; text-transform: uppercase; line-height: 1; white-space: nowrap; }
  .brand-tagline { position: absolute; left: 0; right: 0; top: 125px; font-size: 9px; letter-spacing: 2.6px; text-transform: uppercase; line-height: 1; white-space: nowrap; }
  .entity-details { position: absolute; right: 288px; top: 162px; text-align: right; color: var(--ink); font-size: 13.5px; line-height: 19.8px; }
  .footer-text { position: absolute; color: var(--paper); white-space: nowrap; }
  .licensee { left: 290px; top: 872px; font-size: 13px; line-height: 16.9px; }
  .office { left: 593px; top: 872px; font-size: 10.5px; line-height: 14.2px; }
  .contact { left: 775px; top: 872px; font-size: 10.5px; line-height: 14.2px; }
  .motto { left: 670px; top: 955px; font-size: 16px; font-weight: 700; }
</style>
</head>
<body>
<main class="letterhead">
  <svg class="shapes" viewBox="0 0 1200 1000" aria-hidden="true">
    <path class="header-band" fill="var(--slate)" d="M245,2 H958 V150 H725 C665,150 670,70 620,70 H245 Z"/>
    <circle class="brand-circle" cx="805" cy="72" r="28" fill="none" stroke="var(--paper)" stroke-width="2"/>
    <path class="footer-band" fill="var(--charcoal)" d="M245,858 H915 Q958,858 958,900 V990 H245 Z"/>
    <path class="footer-swoosh" fill="none" stroke="var(--paper)" stroke-width="4" d="M485,858 C532,858 540,938 590,938 H770"/>
    <path class="footer-swoosh" fill="none" stroke="var(--paper)" stroke-width="4" d="M688,858 C735,858 745,938 790,938 H958"/>
  </svg>

  <div class="brand">
    <span class="brand-name">Calderstone Wealth</span>
    <span class="brand-tagline">Strategic Financial Advice</span>
  </div>

  <p class="entity-details">
    Halvern Investments Pty Ltd<br>
    ATF The Westmoor Investment<br>
    Trust T/AS Brightmere Financial<br>
    ABN: 52 318 604 917<br>
    Corporate Authorised<br>
    Representative of Keystone<br>
    Advisory Group Limited
  </p>

  <footer>
    <p class="footer-text licensee">
      Keystone Advisory Group Limited<br>
      ABN 48 107 553 826<br>
      Australian Financial Services Licence<br>
      Licence Number 318 442<br>
      Principle Address: 420 Harbour St<br>
      PO Box 5140 Melbourne VIC 3001
    </p>
    <p class="footer-text office">
      Suite 7A, 15 Ferris St<br>
      Kangaroo Point QLD 4169<br>
      PO Box 4412<br>
      East Brisbane QLD 4169
    </p>
    <p class="footer-text contact">
      p (07) 3555 0182<br>
      f (07) 3555 0199<br>
      www.brightmerefinancial.com.au<br>
      admin@brightmerefinancial.com.au
    </p>
    <p class="footer-text motto">'Financial peace of mind'</p>
  </footer>
</main>
</body>
</html>
```